Brochure Cover and Back pages

We are a US-based cosmetics company that sells state-of-the-art skin care products, including advanced anti-aging serums, natural mineral sunscreens, organic antioxidant moisturizers, and organic face cleansers. We need a product brochure. We already have chosen a design for the layout of the product info pages. But we still need a cover page and a back page. We are looking for simple but elegant design for the cover page. The back page is less important and we already know what we want on the back page. It will be the company's mission statement and at the bottom, the company URL, phone number, etc.

The brochure has two folds. So there will be three panels on both sides. The size of each panel is 16.5 (l) x 9.5 (w) cm.

At the end of the project, we expect the designer to integrate all the pages so that the finished copy is read to be sent off to a printing service for printing.

All the product info pages are attached. Also attached are the text (info) to go on the back page, company logo with and without the tagline, the icon in the logo.

YOu are welcome to visit our website www.corvanyx.com to learn about our products.

Industry/Entity Type

Cosmetics

```html
<!DOCTYPE html>
<html lang="en">
<head>
<meta charset="utf-8">
<title>Corvanyx Brochure – Cover and Back</title>
<link rel="stylesheet" href="https://fonts.googleapis.com/css2?family=Delius&family=Tinos:wght@400;700&family=Arimo&display=swap">
<style>
  :root {
    --stage: #dcdcde;
    --label: #111111;
    --satin-dark: #080908;
    --satin-mid: #1d211e;
    --satin-sheen: rgba(120,128,120,.38);
    --satin-soft: rgba(90,98,90,.3);
    --band: #ffffff;
    --ink: #1a1a1a;
    --contact: #f2f2f2;
    --mark-grey: #a3a3a3;
    --mission-pink: #d36b98;
  }
  * { margin: 0; padding: 0; box-sizing: border-box; }
  html, body { width: 1200px; height: 848px; overflow: hidden; }
  body { background: var(--stage); position: relative; }

  .page-label {
    position: absolute; top: 22px; width: 384px; text-align: center;
    font-family: "Arimo", Arial, sans-serif; font-size: 46px; color: var(--label);
  }
  .page-label--cover { left: 161px; }
  .page-label--back { left: 664px; }

  .panel {
    position: absolute; top: 91px; width: 384px; height: 666px;
    background: var(--band); overflow: hidden;
  }
  .panel--cover { left: 168px; }
  .panel--back { left: 671px; }

  .satin {
    position: absolute; left: 0; top: 0; width: 100%; height: 560px;
    background:
      linear-gradient(155deg, transparent 8%, var(--satin-sheen) 13%, transparent 19%),
      linear-gradient(20deg, transparent 30%, var(--satin-soft) 36%, transparent 42%),
      linear-gradient(140deg, transparent 44%, var(--satin-sheen) 50%, transparent 56%),
      linear-gradient(30deg, transparent 60%, var(--satin-soft) 66%, transparent 72%),
      linear-gradient(165deg, transparent 74%, var(--satin-sheen) 80%, transparent 86%),
      radial-gradient(ellipse 45% 20% at 25% 18%, rgba(110,118,110,.35), transparent 70%),
      radial-gradient(ellipse 40% 18% at 75% 48%, rgba(100,108,100,.3), transparent 70%),
      radial-gradient(ellipse 50% 20% at 30% 85%, rgba(90,96,90,.3), transparent 70%),
      linear-gradient(160deg, var(--satin-mid), var(--satin-dark) 55%, var(--satin-mid));
  }

  .cover-brand {
    position: absolute; left: 17px; top: 586px;
    font-family: "Tinos", "Times New Roman", serif; font-weight: 700;
    font-size: 34px; color: var(--ink); letter-spacing: .5px;
  }
  .cover-tagline {
    position: absolute; left: 24px; top: 629px;
    font-family: "Delius", cursive; font-size: 12px; color: var(--ink);
  }
  .cover-url {
    position: absolute; right: 8px; top: 628px;
    font-family: "Tinos", "Times New Roman", serif; font-size: 14px; color: var(--ink);
  }

  .back-mark {
    position: absolute; left: 0; top: 150px; width: 100%; text-align: center;
    font-family: "Tinos", "Times New Roman", serif; font-weight: 700;
    font-size: 52px; color: var(--mark-grey);
  }

  .contact-list { position: absolute; left: 7px; top: 352px; list-style: none; }
  .contact-item {
    display: flex; align-items: flex-start; gap: 8px; margin-bottom: 31px;
    font-family: "Delius", cursive; font-size: 20px; line-height: 24px;
    color: var(--contact); letter-spacing: 1.2px;
  }
  .contact-icon { width: 28px; height: 24px; flex: none; }

  .mission {
    position: absolute; left: 0; top: 578px; width: 100%; text-align: center;
    font-family: "Delius", cursive; font-size: 23px; line-height: 27px;
    color: var(--mission-pink); letter-spacing: .8px;
  }
</style>
</head>
<body>
  <div class="page-label page-label--cover">cover</div>
  <div class="page-label page-label--back">back</div>

  <section class="panel panel--cover">
    <div class="satin" role="img" aria-label="Dark draped black satin fabric photograph"></div>
    <div class="cover-brand">Corvanyx</div>
    <div class="cover-tagline">Bringing You Smart Skin Care</div>
    <div class="cover-url">www.corvanyx.com</div>
  </section>

  <section class="panel panel--back">
    <div class="satin" role="img" aria-label="Dark draped black satin fabric photograph"></div>
    <div class="back-mark">Corvanyx</div>
    <ul class="contact-list">
      <li class="contact-item">
        <svg class="contact-icon" viewBox="0 0 28 24" fill="none" stroke="currentColor" stroke-width="2">
          <rect x="5" y="3" width="18" height="13" rx="1"/>
          <path d="M2 20h24l-2-3H4z" fill="currentColor"/>
        </svg>
        <span>www.Corvanyx.com</span>
      </li>
      <li class="contact-item">
        <svg class="contact-icon" viewBox="0 0 28 24" fill="none" stroke="currentColor" stroke-width="2">
          <path d="M14 3c6 0 10 3.5 10 8s-4 8-10 8c-1.5 0-3-.2-4-.6L4 21l1.8-4.4C4.6 15 4 13 4 11c0-4.5 4-8 10-8z"/>
          <path d="M9 9h10M9 13h7"/>
        </svg>
        <span>855-555-0142</span>
      </li>
      <li class="contact-item">
        <svg class="contact-icon" viewBox="0 0 28 24" fill="none" stroke="currentColor" stroke-width="2">
          <path d="M3 12L14 3l11 9"/>
          <path d="M6 10v11h16V10"/>
          <rect x="12" y="14" width="4" height="7"/>
        </svg>
        <span>2190 Larkmont Ave.&nbsp; Suite 400<br>Fairbrook, CA 94019</span>
      </li>
    </ul>
    <p class="mission">Creating Beauty Solutions<br>through Science</p>
  </section>
</body>
</html>
```